Visitenkarten-Design für Immobilienprojektmanagement
Zielgruppe
Immobilienprojektmanagement, Immobilienverkauf, Immobilienvermietung
Aufgabenstellung
www.ru-baufolio.de

```html
<!DOCTYPE html>
<html lang="de">
<head>
<meta charset="utf-8">
<title>RU Baufolio – Visitenkarte</title>
<link rel="stylesheet" href="https://fonts.googleapis.com/css2?family=Open+Sans:wght@400;600;700&display=swap">
<style>
  :root {
    --green: #8dbd3c;
    --dark: #3f4042;
    --white: #ffffff;
    --ink: #1d1d1d;
    --stage: #e9e7e2;
  }
  html, body {
    margin: 0;
    padding: 0;
    width: 1200px;
    height: 822px;
    overflow: hidden;
    background: var(--stage);
    font-family: "Open Sans", Arial, sans-serif;
  }
  .stage {
    position: relative;
    width: 1200px;
    height: 822px;
  }
  .card {
    position: absolute;
    top: 252px;
    width: 540px;
    height: 318px;
    box-shadow: 0 6px 18px rgba(0,0,0,0.18);
    overflow: hidden;
  }
  /* Front */
  .card-front {
    left: 40px;
    background: var(--green);
  }
  .front-brand {
    position: absolute;
    left: 0;
    right: 0;
    top: 110px;
    display: flex;
    justify-content: center;
    align-items: center;
    gap: 16px;
  }
  .brand-square {
    width: 38px;
    height: 38px;
    background: var(--dark);
  }
  .front-brand .brand-name {
    font-weight: 700;
    font-size: 52px;
    color: var(--white);
    letter-spacing: 0.5px;
    line-height: 1;
  }
  .tagline {
    position: absolute;
    left: 0;
    right: 0;
    bottom: 52px;
    text-align: center;
    color: var(--white);
    font-size: 13px;
    letter-spacing: 1px;
  }
  /* Back */
  .card-back {
    left: 620px;
    background: var(--white);
  }
  .back-bands {
    position: absolute;
    left: 0;
    bottom: 0;
    width: 540px;
    height: 40px;
  }
  .back-brand {
    position: absolute;
    left: 40px;
    top: 110px;
    display: flex;
    align-items: center;
    gap: 10px;
  }
  .back-brand .brand-square {
    width: 24px;
    height: 24px;
  }
  .back-brand .brand-name {
    font-weight: 700;
    font-size: 30px;
    color: var(--green);
    line-height: 1;
  }
  .services {
    position: absolute;
    left: 50px;
    top: 160px;
    margin: 0;
    padding: 0;
    list-style: none;
    font-size: 14px;
    color: var(--ink);
    line-height: 1.45;
    letter-spacing: 0.4px;
  }
  .services li::before {
    content: "";
    display: inline-block;
    width: 5px;
    height: 5px;
    border-radius: 50%;
    background: var(--green);
    margin-right: 8px;
    vertical-align: middle;
  }
  .divider {
    position: absolute;
    left: 292px;
    top: 52px;
    width: 1px;
    height: 190px;
    background: var(--green);
  }
  .contact {
    position: absolute;
    left: 316px;
    top: 46px;
    font-size: 12.5px;
    color: var(--ink);
    line-height: 1.5;
  }
  .contact .person {
    font-weight: 700;
    font-size: 19px;
    color: var(--green);
    line-height: 1.2;
  }
  .contact .role { margin-bottom: 2px; }
  .contact-lines {
    margin: 6px 0 0;
    padding: 0;
    list-style: none;
  }
  .contact-lines li {
    display: flex;
    align-items: center;
    gap: 8px;
  }
  .contact-lines svg {
    width: 12px;
    height: 12px;
    flex: none;
  }
</style>
</head>
<body>
<main class="stage">

  <section class="card card-front" aria-label="Visitenkarte Vorderseite">
    <div class="front-brand">
      <span class="brand-square"></span>
      <span class="brand-name">RU Baufolio</span>
    </div>
    <p class="tagline">Ihr Immobilienpartner in der Regio</p>
  </section>

  <section class="card card-back" aria-label="Visitenkarte Rückseite">
    <div class="back-brand">
      <span class="brand-square"></span>
      <span class="brand-name">RU Baufolio</span>
    </div>
    <ul class="services">
      <li>Immobilienverkauf</li>
      <li>Vermietung</li>
      <li>Projektmanagement</li>
    </ul>

    <div class="divider"></div>

    <div class="contact">
      <div class="person">Jonas Merten</div>
      <div class="role">Geschäftsführer</div>
      <div>RU-Baufolio e.K.</div>
      <div>Lindenhofweg 7b</div>
      <div>79312 Hallbrunn</div>
      <ul class="contact-lines">
        <li>
          <svg viewBox="0 0 12 12"><path d="M2.5 1h2l1 2.6-1.3 1A6 6 0 0 0 7.4 7.8l1-1.3L11 7.5v2c0 .8-.7 1.5-1.5 1.5A8.5 8.5 0 0 1 1 2.5C1 1.7 1.7 1 2.5 1z" fill="var(--green)"/></svg>
          07441 / 38 20 500
        </li>
        <li>
          <svg viewBox="0 0 12 12"><rect x="3" y="0.8" width="6" height="10.4" rx="1" fill="none" stroke="var(--green)" stroke-width="1.2"/><circle cx="6" cy="9.4" r="0.7" fill="var(--green)"/></svg>
          0171 / 427 6100
        </li>
        <li>
          <svg viewBox="0 0 12 12"><rect x="0.8" y="2.5" width="10.4" height="7" fill="none" stroke="var(--green)" stroke-width="1.2"/><path d="M1 3l5 3.8L11 3" fill="none" stroke="var(--green)" stroke-width="1.2"/></svg>
          info@ru-baufolio.de
        </li>
        <li>
          <svg viewBox="0 0 12 12"><circle cx="6" cy="6" r="5.2" fill="var(--green)"/><path d="M1 6h10M6 .8c-2 2.5-2 7.9 0 10.4M6 .8c2 2.5 2 7.9 0 10.4" fill="none" stroke="var(--white)" stroke-width="0.8"/></svg>
          www.ru-baufolio.de
        </li>
      </ul>
    </div>

    <svg class="back-bands" viewBox="0 0 540 40" preserveAspectRatio="none" aria-hidden="true">
      <polygon points="0,28 340,28 345,20 540,20 540,40 0,40" fill="var(--green)"/>
      <polygon points="352,20 540,0 540,22 345,22" fill="var(--dark)"/>
    </svg>
  </section>

</main>
</body>
</html>
```